https://velormark.com

We need a cool technology design for our Managed IT Services company. We are located in Coral Springs Florida. We provide all IT services and support for small to medium sized businesses. We would like to see designs that use our blue and white colors from our website.

```html
<!DOCTYPE html>
<html lang="en">
<head>
<meta charset="utf-8">
<title>Velormark Business Card</title>
<link rel="stylesheet" href="https://fonts.googleapis.com/css2?family=Signika:wght@400;600&family=Roboto:wght@400&display=swap">
<style>
  :root {
    --backdrop: #e4e2de;
    --card: #f3f2ef;
    --card-edge: #d9d7d2;
    --ink: #1c2b45;
    --ink-soft: #2e3a4f;
  }
  * { margin: 0; padding: 0; box-sizing: border-box; }
  html, body {
    width: 1200px;
    height: 1054px;
    overflow: hidden;
    background: var(--backdrop);
  }
  .business-card {
    position: absolute;
    left: 100px;
    top: 224px;
    width: 1000px;
    height: 605px;
    background: var(--card);
    border: 1px solid var(--card-edge);
    border-radius: 4px;
    color: var(--ink);
  }
  .holder-name {
    position: absolute;
    left: 51px;
    top: 100px;
    font-family: "Signika", sans-serif;
    font-weight: 600;
    font-size: 39px;
    line-height: 1;
  }
  .holder-title {
    position: absolute;
    left: 53px;
    top: 151px;
    font-family: "Roboto", sans-serif;
    font-size: 21px;
    color: var(--ink-soft);
  }
  .brand-name {
    position: absolute;
    right: 62px;
    top: 114px;
    font-family: "Signika", sans-serif;
    font-weight: 600;
    font-size: 78px;
    line-height: 1;
    letter-spacing: -1px;
    color: var(--ink);
  }
  .contact-list {
    position: absolute;
    left: 52px;
    top: 421px;
    list-style: none;
    font-family: "Roboto", sans-serif;
    font-size: 24px;
    color: var(--ink);
  }
  .contact-item {
    display: flex;
    align-items: center;
    height: 35.5px;
  }
  .contact-icon {
    width: 22px;
    height: 22px;
    margin-right: 23px;
    fill: var(--ink);
    stroke: var(--ink);
  }
  .contact-address {
    position: absolute;
    left: 50px;
    top: 537px;
    font-family: "Roboto", sans-serif;
    font-size: 24px;
    color: var(--ink);
  }
</style>
</head>
<body>
  <article class="business-card">
    <h1 class="holder-name">Daniel Reyes Ward</h1>
    <p class="holder-title">Managing Director</p>

    <div class="brand-name">VELORMARK</div>

    <ul class="contact-list">
      <li class="contact-item">
        <svg class="contact-icon" viewBox="0 0 24 24" aria-hidden="true">
          <path stroke="none" d="M3 8c0-2 4-4 9-4s9 2 9 4v2h-5V8.5c-2-.7-6-.7-8 0V10H3z"/>
          <path stroke="none" d="M6 12h12l2 8H4z"/>
        </svg>
        <span>(954) 555-0148</span>
      </li>
      <li class="contact-item">
        <svg class="contact-icon" viewBox="0 0 24 24" aria-hidden="true">
          <rect x="2" y="5" width="20" height="14" stroke="none"/>
          <path d="M2.5 5.5 12 13l9.5-7.5" fill="none" stroke="#f3f2ef" stroke-width="1.8"/>
        </svg>
        <span>www.velormark.com</span>
      </li>
      <li class="contact-item">
        <svg class="contact-icon" viewBox="0 0 24 24" aria-hidden="true" fill="none">
          <circle cx="12" cy="12" r="9" fill="none" stroke-width="2"/>
          <ellipse cx="12" cy="12" rx="4" ry="9" fill="none" stroke-width="1.6"/>
          <path d="M3 12h18M5 7.5h14M5 16.5h14" stroke-width="1.6"/>
        </svg>
        <span>support@velormark.com</span>
      </li>
    </ul>

    <p class="contact-address">2280 Palm Crest Blvd #410 Coral Springs, Florida 33065</p>
  </article>
</body>
</html>
```